Business Card Design Project

We need a business card for our IT services provider business. We provide services to small and medium business, and would like something that reflects the color scheme / branding on our recently updated website - www.tallobrix.com.au

The card type we have chosen is a matte laminated double sided configuration at 86mm x 54mm on 350 GSM cardboard.
Updates

Target Market(s)

Small and Medium Business owners

Industry/Entity Type

Business

Requirements
Must have
• *Details on all cards*

Company Name: Tallobrix Pty Ltd
ABN: 52 683 914 207
Address: 47-49 Pembury Street, Ashcombe Vale, Victoria 3172
Phone: 1300 GRAB UP
Fax: 03 9417 6258
Website: www.tallobrix.com.au
Logo/Handprint Icon

*Person Specific*

```html
<!DOCTYPE html>
<html lang="en">
<head>
<meta charset="utf-8">
<title>Tallobrix Business Card</title>
<link rel="stylesheet" href="https://fonts.googleapis.com/css2?family=Cinzel:wght@400&family=Kaushan+Script&display=swap">
<style>
  :root {
    --card-navy: #1b3f52;
    --lime: #b8d12b;
    --logo-grey: #c9c9c9;
    --accent-blue: #2f6fa8;
    --ink-dark: #1a1a1a;
    --ink-light: #ffffff;
    --stage-light: #cfcfcf;
    --stage-mid: #6b6b6b;
    --stage-dark: #1c1c1c;
  }
  html, body {
    margin: 0;
    padding: 0;
    overflow: hidden;
  }
  .stage {
    position: relative;
    width: 1200px;
    height: 1194px;
    background: linear-gradient(60deg, var(--stage-light) 0%, var(--stage-mid) 55%, var(--stage-dark) 100%);
    overflow: hidden;
  }
  .card {
    position: absolute;
    width: 806px;
    height: 506px;
    background: var(--card-navy);
    border: 1px solid #0d1f29;
    border-top-right-radius: 62px;
    box-sizing: border-box;
    overflow: hidden;
  }
  .card--front { left: 51px; top: 60px; }
  .card--back { left: 352px; top: 610px; }

  .brand {
    position: absolute;
    left: 60px;
    top: 330px;
    display: flex;
    align-items: center;
    gap: 28px;
  }
  .brand__dot {
    width: 70px;
    height: 70px;
    border-radius: 50%;
    background: var(--accent-blue);
  }
  .brand__name {
    font-family: "Cinzel", "Times New Roman", serif;
    font-weight: 400;
    font-size: 112px;
    line-height: 1;
    color: var(--logo-grey);
  }

  .highlight {
    position: absolute;
    left: 0;
    top: 0;
  }
  .person {
    position: absolute;
    left: 54px;
    top: 88px;
    font-family: "Kaushan Script", "Brush Script MT", cursive;
    color: var(--ink-dark);
    font-size: 25px;
    line-height: 38px;
  }
  .person__name { font-size: 29px; letter-spacing: 2px; }

  .company {
    position: absolute;
    left: 474px;
    top: 160px;
    margin: 0;
    font-family: "Kaushan Script", "Brush Script MT", cursive;
    color: var(--ink-light);
    font-size: 22px;
    font-style: normal;
    line-height: 42px;
  }
  .company__line { display: block; white-space: nowrap; }
  .company__indent { padding-left: 164px; }
  .company__gap { margin-top: 8px; }
</style>
</head>
<body>
<main class="stage">
  <section class="card card--front" aria-label="Card front">
    <div class="brand">
      <span class="brand__dot"></span>
      <span class="brand__name">Tallobrix</span>
    </div>
  </section>

  <section class="card card--back" aria-label="Card back">
    <svg class="highlight" width="480" height="260" viewBox="0 0 480 260" aria-hidden="true">
      <circle cx="322" cy="120" r="105" fill="var(--lime)" stroke="#0d1f29" stroke-width="1.5"/>
      <circle cx="149" cy="118" r="125" fill="var(--lime)" stroke="#0d1f29" stroke-width="1.5"/>
      <circle cx="322" cy="120" r="105" fill="var(--lime)"/>
    </svg>
    <div class="person">
      <div class="person__name">XXXX XXXXX</div>
      <div class="person__phone">88514 60273</div>
      <div class="person__email">xxxx.tallobrix.com</div>
    </div>
    <address class="company">
      <span class="company__line">Tallobrix</span>
      <span class="company__line">ABN: 52 683 914 207</span>
      <span class="company__line">Address: 47-49 Pembury Street,</span>
      <span class="company__line company__indent">Ashcombe Vale,</span>
      <span class="company__line company__indent">Victoria 3172</span>
      <span class="company__line company__gap">Phone: 1300 GRAB UP</span>
      <span class="company__line">Fax: 03 9417 6258</span>
      <span class="company__line">Website: www.tallobrix.com.au</span>
    </address>
  </section>
</main>
</body>
</html>
```